Web Design Project

We have screen protector brand for mobile phone and we need
Looking for talented web designer. We need only graphic design of 3 page design Home, Catalog page and Product page

- Home page
- There will be rotating banners on the home page
- Top menu will have Hot products, Screen Protectors, Videos, Contact us
- Screen Protectors will be submenu
- Website will be two languages so put US and Turkish flags on the corner so users will be able to switch
- Home page, there will be newest products and hot products and also one video

I also live any additional creative idea for the website
There will be one inner page and catalog page

Check existing page www.durvelo.com which looks pretty bad. You can take logo from there. If you need logo separate i can send it.

I have attached the layout but feel free to change it. I only try to give idea what i wanna see on it.

```html
<!DOCTYPE html>
<html lang="en">
<head>
<meta charset="utf-8">
<title>Durvelo – Screen Protectors</title>
<link href="https://fonts.googleapis.com/css2?family=Oswald:wght@400;500&family=Open+Sans:wght@400;600;700&display=swap" rel="stylesheet">
<style>
:root{
  --orange:#ee5a1f;
  --blue:#1f8ef1;
  --text:#333;
  --muted:#777;
  --line:#e4e4e4;
  --page-bg:#ececec;
  --footer:#4a4a4a;
  --footer-text:#eee;
}
*{box-sizing:border-box;margin:0;padding:0}
html,body{width:733px;height:1200px;overflow:hidden}
body{background:var(--page-bg);font-family:"Open Sans",Arial,sans-serif;color:var(--text);font-size:10px}
.page{position:relative;width:733px;height:1200px;
  background:repeating-linear-gradient(45deg,#eee 0 2px,#e6e6e6 2px 4px)}
.sheet{position:absolute;left:91px;top:0;width:552px;height:1200px;background:#fff}
.abs{position:absolute}
.top-rule{left:112px;top:0;width:509px;height:5px;background:var(--orange)}
.account-links{right:112px;top:6px;font-size:8.5px;color:#555;display:flex;gap:10px;align-items:center}
.account-links span+span{border-left:1px solid #ccc;padding-left:10px}
.account-links .signup{color:var(--orange);font-weight:600}
.brand{left:117px;top:36px;display:flex;align-items:center;gap:6px;font-family:"Open Sans",sans-serif;font-weight:700;font-size:22px;letter-spacing:1px;color:#2b2b2b}
.brand i{width:12px;height:12px;background:var(--orange);display:block}
.search-label{left:419px;top:36px;font-family:Oswald,sans-serif;color:var(--blue);font-size:12px}
.search{left:461px;top:32px;width:147px;height:23px;border:1px solid #ccc;border-radius:3px;font-size:8px;color:#aaa;font-style:italic;padding:6px 7px}
.search svg{position:absolute;right:5px;top:4px}
.lang{right:112px;top:63px;font-size:8px;color:#aaa}
.lang b{color:var(--orange);font-weight:400}
.nav{left:112px;top:88px;width:509px;height:25px;background:#f1f1f1;display:flex;align-items:center;font-family:Oswald,sans-serif;font-size:12px;color:#333}
.nav .home{width:21px;height:25px;background:var(--orange);display:flex;align-items:center;justify-content:center}
.nav a{padding:0 8px;height:25px;line-height:25px;text-decoration:none;color:#333}
.nav a.active{background:var(--blue);color:#fff;margin-left:4px}
.social{position:absolute;right:8px;top:5px;display:flex;gap:4px}
.social i{width:15px;height:15px;border-radius:50%;display:block}
.hero{left:112px;top:125px;width:509px;height:286px;background:linear-gradient(120deg,#1f2a3c 0%,#3b4a63 45%,#1b2433 100%)}
.panel{background:rgba(120,126,138,.78);color:#fff;padding:10px 10px}
.panel h2{font-family:Oswald,sans-serif;font-weight:400;color:var(--orange);font-size:16px;margin-bottom:4px}
.panel p{font-family:Oswald,sans-serif;font-size:13px;line-height:17px;font-weight:400}
.panel b{font-weight:500}
.panel-1{left:365px;top:144px;width:236px;height:139px}
.panel-2{left:365px;top:291px;width:236px;height:104px}
.btn{background:var(--blue);color:#fff;font-size:9px;display:inline-block;padding:5px 10px}
.panel-1 .btn{position:absolute;right:10px;bottom:10px;padding:6px 11px}
.progress{left:112px;top:413px;width:509px;height:11px;display:flex;gap:2px}
.progress span{flex:1;background:#ddd}
.progress span:first-child{background:var(--orange)}
.sec-title{font-family:Oswald,sans-serif;color:var(--blue);font-size:14px;font-weight:400}
.rule{height:1px;background:var(--line)}
.card{top:480px;width:118px;height:165px;border:3px solid #f0f0f0;background:#fff}
.card .shot{position:absolute;left:25px;top:8px;width:62px;height:96px;border-radius:4px;background:linear-gradient(160deg,#444,#111 60%,#3a6a2a)}
.card .name{position:absolute;top:111px;width:100%;text-align:center;font-size:8px;color:#555}
.card .price{position:absolute;left:7px;bottom:12px;color:var(--orange);font-weight:700;font-size:13px}
.card .btn{position:absolute;right:7px;bottom:11px;font-size:8px;padding:4px 6px}
.card .hover-info{position:absolute;left:8px;top:8px;width:96px;font-size:7.5px;line-height:16px;text-align:center;color:#444}
.video{left:114px;top:711px;width:248px;height:185px;border:3px solid #eee;background:linear-gradient(135deg,#7fa75c,#b9cf97 55%,#6d9a4a)}
.video .play{position:absolute;left:98px;top:66px}
.video-text{left:112px;top:912px;width:251px;border-left:3px solid #eee;padding-left:9px;font-size:8.8px;line-height:13px;color:#666;text-align:justify}
.why-intro{left:392px;top:712px;font-size:9px;line-height:14px;color:#333}
.benefit{left:392px;width:229px;display:flex;gap:9px}
.benefit .icon{flex:0 0 40px;height:40px;border-radius:50%;background:#e4e4e4;display:flex;align-items:center;justify-content:center;border:2px solid #f2f2f2;box-shadow:0 0 0 1px #ddd}
.benefit h3{font-family:Oswald,sans-serif;color:var(--orange);font-weight:400;font-size:11px}
.benefit p{font-size:9px;line-height:12.5px;color:#444}
.benefit-sep{left:440px;width:181px;height:1px;background:var(--line)}
.footer{left:91px;top:1013px;width:552px;height:166px;background:var(--footer);color:var(--footer-text)}
.fcol{position:absolute;top:11px;font-size:8.5px;line-height:14px}
.fcol h4{font-family:Oswald,sans-serif;color:var(--orange);font-weight:400;font-size:11px;margin-bottom:7px}
.fcol b{font-weight:600}
.news-input{width:120px;height:16px;background:#fff;color:#aaa;font-size:7px;font-style:italic;padding:3px 5px;margin-top:6px}
.news-btn{display:inline-block;background:var(--blue);color:#fff;font-size:8px;padding:2px 9px;margin:5px 0 0 67px}
.bottom{left:112px;top:1184px;width:509px;font-size:8px;color:#333;display:flex;justify-content:space-between}
</style>
</head>
<body>
<div class="page">
  <div class="sheet"></div>
  <div class="abs top-rule"></div>
  <div class="abs account-links"><span>MY ACCOUNT</span><span>&#128722; MY CART</span><span class="signup">SIGN UP</span></div>
  <div class="abs brand"><i></i>DURVELO</div>
  <div class="abs search-label">SEARCH:</div>
  <div class="abs search">type your keyword here...
    <svg width="13" height="13" viewBox="0 0 13 13"><circle cx="5" cy="5" r="3.8" fill="none" stroke="#ee5a1f" stroke-width="2"/><path d="M8 8l4 4" stroke="#ee5a1f" stroke-width="2.2"/></svg>
  </div>
  <div class="abs lang"><b>english</b> | turkish</div>

  <nav class="abs nav">
    <span class="home"><svg width="13" height="12" viewBox="0 0 13 12"><path d="M6.5 0L0 6h2v6h3.5V8h2v4H11V6h2z" fill="#fff"/></svg></span>
    <a class="active">HOT PRODUCTS</a><a>SCREEN PROTECTORS</a><a>VIDEOS</a><a>CONTACT US</a>
    <div class="social"><i style="background:#3b5998"></i><i style="background:#2aa9e0"></i><i style="background:#dd4b39"></i></div>
  </nav>

  <div class="abs hero" role="img" aria-label="Photo of a hand in a suit sleeve holding a black smartphone"></div>
  <div class="abs panel panel-1">
    <h2>Cool Screen Protectors</h2>
    <p>- Anti-<b>scratch</b><br>- Anti-<b>fingerprint</b><br>- Washable<br>- Easy to <b>Apply</b></p>
    <span class="btn">watch a video</span>
  </div>
  <div class="abs panel panel-2">
    <h2>Free shipping</h2>
    <p>On order over <b>$29.98</b><br>(lower 48 states only)</p>
  </div>
  <div class="abs progress"><span></span><span></span><span></span></div>

  <div class="abs sec-title" style="left:112px;top:447px">NEW PRODUCTS</div>
  <svg class="abs" style="left:583px;top:451px" width="38" height="12" viewBox="0 0 38 12"><path d="M7 1L2 6l5 5M27 1l5 5-5 5" fill="none" stroke="#1f8ef1" stroke-width="2.2"/></svg>
  <div class="abs rule" style="left:112px;top:469px;width:509px"></div>

  <div class="abs card" style="left:113px">
    <div class="hover-info">This is a hover info box. Here can be a product desc. If the user clicks here, he navigates to another page, where is a larger picture and more details.</div>
    <div class="name">Durvelo NEXA VOLT 3D</div><div class="price">$20.99</div><span class="btn">add to cart</span>
  </div>
  <div class="abs card" style="left:243px">
    <div class="shot" role="img" aria-label="Product photo of a touchscreen phone"></div>
    <div class="name">Durvelo NEXA VOLT 3D</div><div class="price">$15.99</div><span class="btn">add to cart</span>
  </div>
  <div class="abs card" style="left:373px">
    <div class="shot" role="img" aria-label="Product photo of a keyboard phone" style="top:20px;height:70px;left:32px;width:48px"></div>
    <div class="name">Durvelo NEXA VOLT 3D</div><div class="price">$17.99</div><span class="btn">add to cart</span>
  </div>
  <div class="abs card" style="left:503px">
    <div class="shot" role="img" aria-label="Product photo of a keyboard phone with protector film"></div>
    <div class="name">Durvelo NEXA VOLT 3D</div><div class="price">$16.99</div><span class="btn">add to cart</span>
  </div>

  <div class="abs sec-title" style="left:112px;top:674px">WATCH OUR VIDEO PREVIEW</div>
  <div class="abs rule" style="left:112px;top:696px;width:251px"></div>
  <div class="abs video" role="img" aria-label="Video still of hands holding a phone over green grass">
    <svg class="play" width="46" height="46" viewBox="0 0 46 46"><circle cx="23" cy="23" r="20" fill="none" stroke="#fff" stroke-width="4"/><path d="M18 13l14 10-14 10z" fill="#fff"/></svg>
  </div>
  <p class="abs video-text">The preview video shows how our screen protectors work, and how to apply them to your device. Faucibus et congue vel, hendrerit non orci. Nunc lacus felis, accumsan in bibendum et, vehicula et arcu. Vestibulum ullamcorper purus non quam porttitor pellentesque.</p>

  <div class="abs sec-title" style="left:392px;top:674px">WHY CHOOSE US?</div>
  <div class="abs rule" style="left:392px;top:696px;width:229px"></div>
  <p class="abs why-intro">Because we sell high quality screen protectors.<br>Here are our screen protector’s benefits:</p>

  <div class="abs benefit" style="top:746px">
    <div class="icon"><svg width="18" height="20" viewBox="0 0 18 20"><path d="M9 1L2 4v6c0 4 3 7 7 9 4-2 7-5 7-9V4z" fill="#fff" stroke="#999" stroke-width="1.5"/></svg></div>
    <div><h3>ANTI - SCRATCH</h3><p>Anti-scratch is really cool, because maecenas tincidunt nisl eget diam porttitor at vulputate dui egestas. Donec ac elit nisi.</p></div>
  </div>
  <div class="abs benefit-sep" style="top:803px"></div>
  <div class="abs benefit" style="top:809px">
    <div class="icon"><svg width="20" height="20" viewBox="0 0 20 20"><rect x="3" y="3" width="14" height="14" fill="#fff" stroke="#999" stroke-width="1.3"/><path d="M3 3l14 14M17 3L3 17" stroke="#ee5a1f" stroke-width="1.5"/></svg></div>
    <div><h3>ANTI - FINGERPRINT</h3><p>Anty-fingerprint is really cool, because maecenas tincidunt nisl eget diam porttitor at vulputate dui egestas.</p></div>
  </div>
  <div class="abs benefit-sep" style="top:866px"></div>
  <div class="abs benefit" style="top:872px">
    <div class="icon"><svg width="16" height="20" viewBox="0 0 16 20"><path d="M8 1C5 7 2 10 2 13a6 6 0 0012 0C14 10 11 7 8 1z" fill="#999"/></svg></div>
    <div><h3>WASHABLE</h3><p>Our screen protectors are washable, and fermentum pretium nisl. Sed gravida volutpat risus quis suscipit.</p></div>
  </div>
  <div class="abs benefit-sep" style="top:929px"></div>
  <div class="abs benefit" style="top:935px">
    <div class="icon"><svg width="20" height="20" viewBox="0 0 20 20"><path d="M3 15L15 3M9 3h6v6" fill="none" stroke="#999" stroke-width="2"/><path d="M3 17h14" stroke="#ee5a1f" stroke-width="2"/></svg></div>
    <div><h3>EASY TO APPLY</h3><p>Our screen protectors are really easy to apply for your device, ros eu neque ultrices laoreet. Vestibulum lectus justo.</p></div>
  </div>

  <footer class="abs footer">
    <div class="fcol" style="left:21px"><h4>CONTACT US</h4><b>Liman Cad. 18/22 Karakoy<br>/ Istanbul - Turkey</b><br><br>Tel: 0212 555 01 65<br>Fax: 0212 555 01 64<br>Email: info@durvelo.com</div>
    <div class="fcol" style="left:150px"><h4>QUICK LINKS</h4>About Us<br>About screen protectors<br>Privacy Policy<br>Sitemap</div>
    <div class="fcol" style="left:281px"><h4>SUPPORT</h4>How to apply<br>FAQ<br>Warranty<br>Returning policy<br>Unsubscribe</div>
    <div class="fcol" style="left:410px"><h4>NEWSLETTER</h4><b>Fresh news, discounts, sales:</b><div class="news-input">type your e-mail address here...</div><span class="news-btn">subscribe</span></div>
  </footer>
  <div class="abs bottom"><span>Copyright © 2013 Durvelo.com</span><span>All rights reserved.</span></div>
</div>
</body>
</html>
```